Criação de Kit com 5 Layouts de Post para Redes Sociais (Facebook, Instagram e etc) para Construção & Engenharia
A empresa queria:
" Trabalho com a elaboração de projetos de engenharia em geral, sendo o maior foco e experiência os proj. de Prevenção e combate a incêndio, mas tbm na elaboração de projetos arquitetônico, estrutural, e de interiores. Regularização de obras junto a Prefeitura, Corpo de Bombeiros, Junta Ouromar, Vigilância Sanitária. Acompanhamento de Obras. "

```html
<!DOCTYPE html>
<html lang="pt-BR">
<head>
<meta charset="UTF-8">
<title>Regularize seu imóvel</title>
<link href="https://fonts.googleapis.com/css2?family=Montserrat:wght@400;500;600;800&display=swap" rel="stylesheet">
<style>
  :root {
    --green-dark: #2c3a2d;
    --green-mid: #3a4a3a;
    --gold: #c9b27c;
    --gold-light: #e2d3a6;
    --white: #ffffff;
    --sky: #dfe4e6;
  }
  html, body { margin: 0; padding: 0; overflow: hidden; }
  body { width: 1200px; height: 1200px; font-family: "Montserrat", Arial, sans-serif; }
  .post { position: relative; width: 1200px; height: 1200px; overflow: hidden; background: var(--sky); }
  .house-photo {
    position: absolute; left: 0; top: 0; width: 1200px; height: 700px;
    background: linear-gradient(180deg, #eef1f2 0%, #cfd6d8 35%, #8d9493 60%, #5d6157 100%);
  }
  .top-strip { position: absolute; left: 0; top: 0; width: 1200px; height: 40px; }
  .panel { position: absolute; left: 0; top: 0; width: 1200px; height: 1200px; }
  .title {
    position: absolute; left: 84px; top: 62px; margin: 0;
    font-weight: 800; font-size: 74px; line-height: 78px; letter-spacing: 1px;
    color: var(--green-dark); text-transform: uppercase;
  }
  .question {
    position: absolute; left: 96px; top: 650px; margin: 0;
    font-weight: 600; font-size: 35px; line-height: 43px; color: var(--white);
  }
  .divider { position: absolute; left: 96px; top: 812px; width: 640px; height: 60px; }
  .agencies { position: absolute; left: 86px; top: 888px; margin: 0; padding: 0; list-style: none; }
  .agencies li {
    display: flex; align-items: center; gap: 22px; height: 67px;
    font-weight: 400; font-size: 37px; color: var(--white); letter-spacing: 0.5px;
  }
  .agencies svg { width: 56px; height: 52px; flex: none; }
  .consult-photo {
    position: absolute; left: 702px; top: 450px; width: 444px; height: 444px;
    border-radius: 50%; border: 10px solid var(--gold); box-sizing: border-box;
    background: radial-gradient(circle at 45% 40%, #e9e6df 0%, #b9ad97 45%, #5a4a38 100%);
  }
  .brand {
    position: absolute; left: 770px; top: 930px; width: 360px; text-align: center;
    font-weight: 600; font-size: 38px; line-height: 44px; color: var(--gold);
  }
  .contact { position: absolute; left: 770px; top: 1080px; width: 360px; text-align: center; color: var(--white); }
  .contact .label { font-weight: 500; font-size: 24px; letter-spacing: 1px; margin-bottom: 8px; }
  .contact .line { display: flex; justify-content: center; align-items: center; gap: 10px; font-size: 25px; font-weight: 600; height: 36px; }
  .contact .line.email { font-size: 21px; font-weight: 500; }
  .contact svg { width: 26px; height: 26px; }
</style>
</head>
<body>
<div class="post">
  <div class="house-photo" role="img" aria-label="Fotografia de uma casa clara de dois andares com telhado escuro e janelas iluminadas, cercada de árvores"></div>

  <svg class="top-strip" viewBox="0 0 1200 40" aria-hidden="true">
    <polygon points="560,0 1200,0 1200,26 590,26" fill="var(--green-dark)"/>
    <line x1="0" y1="10" x2="540" y2="10" stroke="var(--gold)" stroke-width="3"/>
  </svg>

  <svg class="panel" viewBox="0 0 1200 1200" aria-hidden="true">
    <polygon points="0,560 1200,500 1200,1200 0,1200" fill="var(--green-dark)"/>
    <line x1="0" y1="556" x2="1200" y2="496" stroke="var(--gold)" stroke-width="4"/>
  </svg>

  <h1 class="title">Regularize<br>seu imóvel</h1>

  <div class="consult-photo" role="img" aria-label="Fotografia de mãos assinando um documento sobre uma mesa, com martelo de juiz e balança da justiça ao fundo"></div>

  <p class="question">Está precisando<br>regularizar o seu imóvel<br>junto aos órgãos competentes?</p>

  <svg class="divider" viewBox="0 0 640 60" aria-hidden="true">
    <line x1="0" y1="30" x2="640" y2="30" stroke="var(--gold)" stroke-width="2"/>
    <rect x="470" y="12" width="36" height="36" transform="rotate(45 488 30)" fill="var(--gold)"/>
    <rect x="540" y="20" width="20" height="20" transform="rotate(45 550 30)" fill="var(--gold)"/>
  </svg>

  <ul class="agencies">
    <li><svg viewBox="0 0 56 52" aria-hidden="true"><rect x="3" y="9" width="38" height="38" fill="none" stroke="var(--gold)" stroke-width="4"/><path d="M10 26 L21 38 L50 4" fill="none" stroke="var(--gold)" stroke-width="6" stroke-linecap="square"/></svg>Prefeitura</li>
    <li><svg viewBox="0 0 56 52" aria-hidden="true"><rect x="3" y="9" width="38" height="38" fill="none" stroke="var(--gold)" stroke-width="4"/><path d="M10 26 L21 38 L50 4" fill="none" stroke="var(--gold)" stroke-width="6" stroke-linecap="square"/></svg>Corpo de Bombeiros</li>
    <li><svg viewBox="0 0 56 52" aria-hidden="true"><rect x="3" y="9" width="38" height="38" fill="none" stroke="var(--gold)" stroke-width="4"/><path d="M10 26 L21 38 L50 4" fill="none" stroke="var(--gold)" stroke-width="6" stroke-linecap="square"/></svg>Junta Ouromar</li>
    <li><svg viewBox="0 0 56 52" aria-hidden="true"><rect x="3" y="9" width="38" height="38" fill="none" stroke="var(--gold)" stroke-width="4"/><path d="M10 26 L21 38 L50 4" fill="none" stroke="var(--gold)" stroke-width="6" stroke-linecap="square"/></svg>Vigilância Sanitária</li>
  </ul>

  <div class="brand">Vértice<br>Engenharia</div>

  <div class="contact">
    <div class="label">ENTRE EM CONTATO</div>
    <div class="line">
      <svg viewBox="0 0 26 26" aria-hidden="true"><path d="M7 3 L10 3 L12 8 L9.5 10 C10.5 13 13 15.5 16 16.5 L18 14 L23 16 L23 19 C23 21 21 23 19 23 C10 22 4 16 3 7 C3 5 5 3 7 3 Z" fill="var(--white)"/></svg>
      (31) 98765 4321
    </div>
    <div class="line email">
      <svg viewBox="0 0 26 26" aria-hidden="true"><rect x="2" y="5" width="22" height="16" rx="2" fill="var(--white)"/><path d="M3 6 L13 14 L23 6" fill="none" stroke="var(--green-dark)" stroke-width="2"/></svg>
      contato@verticeeng.com
    </div>
  </div>
</div>
</body>
</html>
```